card design for engineering consultancy

engineering drafting and project management company the provides drafting services for.
Electrical, Hydraulic, Mechanical, and Civil services
The company is called Q7R Services and logo is as attached
Information on card should be.
1. Logo
2.website : Q7RServices.example
3. email : info@Q7RServices.example
4. Phone: (+61) 400512836
5. Motto: Plan - Draft - Build - Handover

this card should be basically used for business identification only

Target Market(s)

electricians plumbers air conditioning installers and civil contractors

Industry/Entity Type

engineering, drafting, electrical, plumbing, airconditioning, civil

Contact Information for Business Card

1. Logo 2.website : Q7RServices.example 3. email : info@Q7RServices.example 4. Phone: (+61) 400512836 5. Motto: Plan - Draft - Build - Handover

Font styles to use
Serif

Requirements
Must have
• logo
Nice to have
• something inovative and different that makes it stand out from being just another business card

```html
<!DOCTYPE html>
<html lang="en">
<head>
<meta charset="utf-8">
<title>Q7R Services – Business Card</title>
<link rel="stylesheet" href="https://fonts.googleapis.com/css2?family=Montserrat:wght@400;500;700&family=Oswald:wght@500&display=swap">
<style>
  :root {
    --backdrop: #2b2b2b;
    --card-dark: #333333;
    --card-light: #ffffff;
    --brand-red: #cc1f27;
    --ink-grey: #4a4a4a;
    --ink-dark: #2a2a2a;
    --faint-block: #f3f3f3;
  }
  * { box-sizing: border-box; margin: 0; padding: 0; }
  html, body { width: 1200px; height: 1186px; overflow: hidden; }
  body {
    background: var(--backdrop);
    font-family: "Montserrat", sans-serif;
    position: relative;
  }
  .card {
    position: absolute;
    width: 720px;
    height: 412px;
    border-radius: 28px;
    overflow: hidden;
  }

  /* Back of card */
  .card--back {
    left: 70px;
    top: 100px;
    background: var(--card-dark);
    border-bottom: 12px solid var(--brand-red);
  }
  .back__wordmark {
    position: absolute;
    left: 0; right: 0; top: 140px;
    display: flex;
    align-items: center;
    justify-content: center;
    gap: 22px;
  }
  .back__mark-square {
    width: 48px; height: 48px;
    background: var(--brand-red);
  }
  .back__name {
    font-weight: 700;
    font-size: 62px;
    letter-spacing: 6px;
    color: var(--card-light);
    text-transform: uppercase;
    white-space: nowrap;
  }
  .back__motto {
    position: absolute;
    left: 0; right: 0; top: 265px;
    display: flex;
    justify-content: center;
    gap: 26px;
    font-family: "Oswald", sans-serif;
    font-weight: 500;
    font-size: 24px;
    letter-spacing: 1px;
    color: var(--card-light);
    list-style: none;
  }
  .back__motto li::before {
    content: "";
    display: inline-block;
    width: 8px; height: 8px;
    border-radius: 50%;
    background: var(--brand-red);
    margin-right: 10px;
    vertical-align: middle;
  }

  /* Front of card */
  .card--front {
    left: 410px;
    top: 650px;
    background: var(--card-light);
  }
  .front__faint-block {
    position: absolute;
    left: 30px; top: 120px;
    width: 240px; height: 260px;
    border-radius: 18px;
    background: var(--faint-block);
  }
  .front__wordmark {
    position: absolute;
    right: 48px; top: 56px;
    display: flex;
    align-items: center;
    gap: 14px;
  }
  .front__mark-square {
    width: 30px; height: 30px;
    background: var(--brand-red);
  }
  .front__name {
    font-weight: 700;
    font-size: 36px;
    letter-spacing: 4px;
    color: var(--ink-grey);
    text-transform: uppercase;
    white-space: nowrap;
  }
  .front__rule {
    position: absolute;
    right: 48px; top: 132px;
    width: 440px; height: 2px;
    background: var(--brand-red);
  }
  .contact {
    position: absolute;
    left: 56px; top: 200px;
    width: 340px;
  }
  .contact__person {
    font-weight: 700;
    font-size: 28px;
    color: var(--brand-red);
  }
  .contact__role {
    font-size: 17px;
    color: var(--ink-dark);
    margin-top: 2px;
  }
  .contact__rule {
    height: 2px;
    background: var(--brand-red);
    margin: 14px 0 16px;
    width: 300px;
  }
  .contact__list { list-style: none; }
  .contact__list li {
    display: flex;
    align-items: center;
    gap: 12px;
    font-size: 17px;
    color: var(--ink-dark);
    margin-bottom: 8px;
    white-space: nowrap;
  }
  .contact__icon { width: 16px; height: 16px; flex: none; }
</style>
</head>
<body>

  <section class="card card--back" aria-label="Card back">
    <div class="back__wordmark">
      <span class="back__mark-square"></span>
      <span class="back__name">Q7R Services</span>
    </div>
    <ul class="back__motto">
      <li>PLAN</li>
      <li>DRAFT</li>
      <li>BUILD</li>
      <li>HANDOVER</li>
    </ul>
  </section>

  <section class="card card--front" aria-label="Card front">
    <div class="front__faint-block"></div>
    <div class="front__wordmark">
      <span class="front__mark-square"></span>
      <span class="front__name">Q7R Services</span>
    </div>
    <div class="front__rule"></div>

    <div class="contact">
      <p class="contact__person">Daniel Harper</p>
      <p class="contact__role">CEO &amp; Founder</p>
      <div class="contact__rule"></div>
      <ul class="contact__list">
        <li>
          <svg class="contact__icon" viewBox="0 0 16 16" aria-hidden="true">
            <path fill="#cc1f27" d="M3 1h3l1.5 4-2 1.2a9 9 0 0 0 4.3 4.3L11 8.5l4 1.5v3a2 2 0 0 1-2 2A12 12 0 0 1 1 3a2 2 0 0 1 2-2z"/>
          </svg>
          (+61) 400512836
        </li>
        <li>
          <svg class="contact__icon" viewBox="0 0 16 16" aria-hidden="true">
            <rect x="1" y="3" width="14" height="10" rx="1.5" fill="#cc1f27"/>
            <path d="M1.5 4l6.5 5 6.5-5" fill="none" stroke="#fff" stroke-width="1.2"/>
          </svg>
          info@Q7RServices.example
        </li>
        <li>
          <svg class="contact__icon" viewBox="0 0 16 16" aria-hidden="true">
            <circle cx="8" cy="8" r="7" fill="#cc1f27"/>
            <path d="M1 8h14M8 1c3 3 3 11 0 14M8 1c-3 3-3 11 0 14" fill="none" stroke="#fff" stroke-width="1"/>
          </svg>
          Q7RServices.example
        </li>
      </ul>
    </div>
  </section>

</body>
</html>
```